Lotvantage.com Webpage Design

Design Brief for lotvantage.com (Copy of Brief also in attached Word file)

Name of Website- lotvantage.com (existing logo and look & feel of website to be changed)

Logo - Finalised. The logo files are attached with the brief as “logo.jpeg”. The “Blue- Grey” version of the logo is for use on lighter backgrounds and the “Orange-White” version of the logo is for use on darker backgrounds. (A full Black version of the logo is also attached). Both versions may be used in different parts of the website. All attached files are in .png format.
Status - The website in functional and is undergoing user trials. However, we want to improve the look & feel of the website so at it seems
a. cotemporary,
b. Easy to Navigate
c. professional and
d. Vibrant.

Please visit ‘lotvantage.com’ to check out the website and its functionalities – please use it only as a reference for the features & functions to be provided, however the designer should use a ‘Free Hand’ in designing the composition of various parts of the webpage without getting too influenced by the existing design

Objective of the Website ‘lotvantage.com –
a. It is a portal focussed on listing of ‘Retail’ specific real-estate properties by developers, owners and realty brokers. The properties shall listed under the following four categories-
i. Retail Malls
ii. Shopping Complexes
iii. High-street shops
iv. Retail Warehouses
*refer lotvantage.com for better clarity

b. The abovementioned properties shall be listed either for ‘Sale’ or ‘rent\lease’ or both

c. Users shall visit the site in case they wish to acquire a retail \ shop space either on ‘sale’ or ‘rent’. These Users would be able to specify the ‘Search Criteria’ through the tool-bars provided on the website – the ‘Search Criteria’ shall comprise of ‘Type of space category’, ‘City’, ‘Locality’, transaction type ie ‘Rent \ Sale’ and ‘Area Range’

d. The main revenue model for the website shall be listing fee ( or advertising charges ) payable by those listing their properties on the website.

Three Main Pages of Website (lotvantage.com) that need to be designed -
a. Main Home Page (visit the web link - http://lotvantage.com/ ) - The main home page has the “Search Toolbar” for specifying of Search Criteria by the User. It shall also have the following features & functions-
i. Main Advertising Banner
ii. Featured Projects
iii. New Launches
iv. Toolbar with buttons – ‘Advertise with Us’, ‘Listings Alert’, ‘Lot Mavens’, ‘Advertiser Login’

b. Property Listings Page (visit the web link - http://lotvantage.com/gurgaon-in-india ) - The List of property options that match the Criteria specified by the ‘User’ get displayed on this page.

c. Property Detail Page - When the ‘User’ clicks on the “More….” Button on the ‘Property Listings Page’ (given in point b. above) the web page with the details of the property opens. (For Example – visit the web link - http://lotvantage.com/brevo-Shopping-Complex-brevo-quadrel-gurgaon-636 )

Note:- Please refer to attached ‘Shopping’ related images the designer may use them on the website to provide a look & feel of retail if required – either separately or rotate in a single window

Target Market(s)

Retailers & Investors looking for retail space, Real Estate Brokers, Developers

Industry/Entity Type

Advertising

Number of Pages Required

3 page

Requirements
Must have
• Refer to existing site lotvantage.com -- all the existing functionalities are a must have.
Nice to have
• The Designer may use the retail related images on the website if required for making it more vibrant. Refer attached images Shopping(1-6).jpg

```html
<!DOCTYPE html>
<html lang="en">
<head>
<meta charset="utf-8">
<title>Lotvantage.com – Retail Property Portal</title>
<link href="https://fonts.googleapis.com/css2?family=Open+Sans:wght@400;600;700;800&display=swap" rel="stylesheet">
<style>
:root{
  --blue:#1b7cc3;
  --blue-dark:#0f5c98;
  --blue-light:#e8f2fa;
  --orange:#f29a2e;
  --ink:#333333;
  --muted:#8a8a8a;
  --line:#dcdcdc;
  --page:#f3f3f3;
  --panel-grey:#7b7b7b;
  --field-dark:#3a3a3a;
  --footer-dark:#1d1d1d;
  --white:#ffffff;
}
*{box-sizing:border-box;margin:0;padding:0}
html,body{width:1200px;height:3130px;overflow:hidden}
body{font-family:"Open Sans",Arial,sans-serif;color:var(--ink);background:var(--white);font-size:13px}
.wrap{width:1030px;margin:0 auto;position:relative;height:100%}

/* header */
.site-header{height:122px;background:var(--white)}
.city-select{position:absolute;right:0;top:4px;width:170px;height:22px;border:1px solid var(--line);font-size:10px;padding:3px 6px;display:flex;justify-content:space-between;align-items:center}
.brand{position:absolute;left:0;top:40px;display:flex;align-items:center;gap:10px}
.brand-dot{width:44px;height:44px;border-radius:50%;background:var(--blue)}
.brand-name{font-size:34px;font-weight:700;color:var(--blue-dark);line-height:1}
.brand-tag{position:absolute;left:54px;top:82px;font-size:9px;color:var(--muted);letter-spacing:.5px;text-transform:uppercase}
.top-actions{position:absolute;right:0;top:58px;display:flex;gap:18px}
.top-actions a{display:block;width:150px;height:32px;line-height:30px;text-align:center;font-size:10px;font-weight:600;text-transform:uppercase;color:var(--ink);border:1px solid var(--orange);text-decoration:none}
.top-actions a.is-highlight{background:var(--blue);color:var(--white);border-color:var(--blue)}

/* nav */
.main-nav{height:45px;background:var(--blue)}
.main-nav ul{list-style:none;display:flex;height:45px;align-items:center}
.main-nav li{color:var(--white);font-size:12px;font-weight:600;text-transform:uppercase;margin-right:44px}
.nav-search{position:absolute;right:0;top:0;width:45px;height:45px;background:var(--blue-dark);display:flex;align-items:center;justify-content:center}

/* hero */
.hero{height:546px;position:relative;overflow:hidden}
.hero-photo{position:absolute;inset:0;background:linear-gradient(100deg,#5d6c7a 0%,#8d7f86 30%,#c26a8f 55%,#7a5a52 78%,#3c3434 100%)}
.search-panel{position:absolute;left:89px;top:50px;width:383px;height:476px;background:rgba(255,255,255,.96);padding:64px 20px 20px}
.search-tab{position:absolute;left:20px;top:-12px;width:300px;height:58px;background:var(--blue);color:var(--white);font-size:22px;font-weight:700;text-align:center;line-height:58px}
.format-list{display:grid;grid-template-columns:1fr 1fr;gap:9px 10px;margin-bottom:14px}
.format-list label{display:flex;align-items:center;gap:6px;font-size:11px;font-weight:600}
.tick{width:12px;height:12px;border:1px solid #777;background:var(--white)}
.field-label{font-size:10px;font-weight:600;margin:8px 0 4px}
.field-dark{height:32px;background:var(--field-dark);color:#ddd;font-size:11px;padding:0 10px;display:flex;align-items:center;justify-content:space-between}
.submit-btn{display:block;margin:18px auto 0;width:230px;height:42px;background:var(--blue);color:var(--white);font-size:20px;font-weight:700;text-align:center;line-height:42px}
.hero-copy{position:absolute;left:530px;top:102px;width:470px;color:var(--white)}
.hero-copy .kicker{font-size:30px;font-weight:700;line-height:1.2}
.hero-copy .headline{font-size:38px;font-weight:800;color:#27a7ff;line-height:1.2}
.hero-copy p{font-size:14px;line-height:1.55;margin-top:14px}
.read-more{display:inline-block;margin-top:26px;background:var(--blue);color:var(--white);font-size:15px;font-weight:600;padding:14px 32px;text-transform:uppercase}

/* listing sections */
.featured{height:714px;background:var(--page);padding-top:30px}
.launches{height:660px;background:var(--blue);padding-top:30px}
.section-title{font-size:21px;font-weight:600;color:var(--ink);margin-bottom:18px}
.launches .section-title{color:var(--white)}
.card-grid{display:grid;grid-template-columns:repeat(4,226px);justify-content:space-between;row-gap:28px}
.card{background:var(--white);height:285px;box-shadow:0 2px 6px rgba(0,0,0,.18);padding:10px;display:flex;flex-direction:column}
.launches .card{height:272px}
.card-photo{height:150px}
.tone-a{background:linear-gradient(180deg,#9fc6e8,#c9c2b5 60%,#8e8a80)}
.tone-b{background:linear-gradient(180deg,#a7c9e6,#d8cdb6 60%,#b39b78)}
.tone-c{background:linear-gradient(180deg,#7ea9d6,#d6d8dc 55%,#8e9aa6)}
.tone-d{background:linear-gradient(180deg,#233a66,#d07b2e 55%,#3b2a2a)}
.tone-e{background:linear-gradient(180deg,#6fa6d6,#c24a4a 55%,#4f4a56)}
.card h3{font-size:15px;font-weight:400;text-align:center;margin-top:8px}
.card .locality{font-size:11px;color:var(--blue);text-align:center}
.card .type{font-size:9px;color:var(--muted);text-align:center;margin-top:2px}
.card-foot{margin-top:auto;display:flex;height:32px}
.card-foot .city{flex:1;background:#e3e3e3;font-size:11px;display:flex;align-items:center;justify-content:center}
.card-foot .view{flex:1.3;background:var(--blue);color:var(--white);font-size:11px;font-weight:600;display:flex;align-items:center;justify-content:center}

/* widgets */
.widgets{height:500px;background:var(--white);padding-top:88px}
.widget-row{display:flex;gap:35px}
.mavens{width:365px;height:385px;background:var(--panel-grey);border-radius:10px;padding:18px;color:var(--white)}
.widget-title{font-size:17px;font-weight:700;margin-bottom:10px}
.mavens p{font-size:10px;line-height:1.5;margin-bottom:14px}
.input{height:30px;background:var(--white);color:#999;font-size:10px;padding:0 10px;display:flex;align-items:center;margin-bottom:10px}
.input.textarea{height:70px;align-items:flex-start;padding-top:8px}
.send{display:inline-block;background:var(--blue);color:var(--white);font-size:12px;font-weight:600;padding:8px 26px;margin-top:6px}
.plain-col{flex:1;padding-top:10px}
.plain-col+.plain-col{border-left:1px solid var(--line);padding-left:30px}
.plain-col p{font-size:11px;line-height:1.6;margin:14px 0 26px;color:#555}
.plain-col .input{background:var(--field-dark);color:#ccc;justify-content:space-between}

/* about footer */
.about-footer{height:283px;background:var(--blue);color:var(--white);padding-top:40px}
.about-cols{display:flex;gap:50px}
.about-cols>div{flex:1}
.about-cols h4{font-size:17px;font-weight:600;margin-bottom:18px}
.about-cols ul{list-style:none;font-size:11px;font-weight:600;line-height:2}
.about-cols p{font-size:11px;line-height:1.6}

/* bottom footer */
.bottom-footer{height:260px;background:var(--footer-dark);color:#ccc;text-align:center;padding-top:44px}
.footer-brand{display:inline-flex;align-items:center;gap:10px}
.footer-brand .brand-dot{width:38px;height:38px;background:var(--orange)}
.footer-brand .brand-name{color:var(--white);font-size:32px}
.footer-links{font-size:11px;margin-top:20px}
.copyright{font-size:11px;margin-top:6px}
.social{display:flex;gap:10px;justify-content:center;margin-top:18px}
.social span{width:26px;height:26px;border-radius:50%;background:#555}
</style>
</head>
<body>

<header class="site-header">
  <div class="wrap">
    <div class="city-select">Select Your City <svg width="8" height="6"><path d="M0 0h8L4 6z" fill="#555"/></svg></div>
    <div class="brand"><span class="brand-dot"></span><span class="brand-name">lotvantage</span></div>
    <div class="brand-tag">India's leading portal for retail space</div>
    <nav class="top-actions">
      <a href="#">Advertise with us</a>
      <a href="#">Listings alert</a>
      <a href="#" class="is-highlight">Lot Mavens</a>
      <a href="#">Advertiser login</a>
    </nav>
  </div>
</header>

<nav class="main-nav">
  <div class="wrap">
    <ul><li>Home</li><li>About Us</li><li>Property Listings</li><li>Property Detail</li></ul>
    <div class="nav-search"><svg width="20" height="20" viewBox="0 0 20 20"><circle cx="8" cy="8" r="6" fill="none" stroke="#fff" stroke-width="2.5"/><path d="M12.5 12.5L18 18" stroke="#fff" stroke-width="3"/></svg></div>
  </div>
</nav>

<section class="hero">
  <div class="hero-photo" role="img" aria-label="Shoppers carrying bags in a bright retail street"></div>
  <div class="wrap">
    <form class="search-panel">
      <div class="search-tab">Select Retail Format</div>
      <div class="format-list">
        <label><span class="tick"></span>Retail Malls</label>
        <label><span class="tick"></span>Shopping Complex</label>
        <label><span class="tick"></span>High Street Shops</label>
        <label><span class="tick"></span>Retail Warehouses</label>
      </div>
      <div class="field-label">Sale Or Rent Or Both</div>
      <div class="field-dark">Both <svg width="8" height="6"><path d="M0 0h8L4 6z" fill="#ccc"/></svg></div>
      <div class="field-label">Select Your City</div>
      <div class="field-dark">Select <svg width="8" height="6"><path d="M0 0h8L4 6z" fill="#ccc"/></svg></div>
      <div class="field-label">Select Locality</div>
      <div class="field-dark">Select <svg width="8" height="6"><path d="M0 0h8L4 6z" fill="#ccc"/></svg></div>
      <div class="field-label">Enter Keywords</div>
      <div class="field-dark">Name of the Project, Developer etc</div>
      <span class="submit-btn">Submit</span>
    </form>
    <div class="hero-copy">
      <div class="kicker">Lorem Ipsum is simply</div>
      <div class="headline">Lorem Ipsum is simply</div>
      <p>Lorem Ipsum is simply dummy text of the printing and typesetting industry. Lorem Ipsum has been the industry's standard dummy text ever since the 1500s.</p>
      <span class="read-more">Read More</span>
    </div>
  </div>
</section>

<section class="featured">
  <div class="wrap">
    <h2 class="section-title">Featured Retail Projects</h2>
    <div class="card-grid">
      <article class="card"><div class="card-photo tone-a" role="img" aria-label="Residential retail tower"></div><h3>Magnora</h3><div class="locality">Adhan</div><div class="type">Shopping Complex</div><div class="card-foot"><span class="city">Surat</span><span class="view">View the listing</span></div></article>
      <article class="card"><div class="card-photo tone-b" role="img" aria-label="High street retail building"></div><h3>Veyra 81 High Street</h3><div class="locality">Sector 81</div><div class="type">Shopping Complex</div><div class="card-foot"><span class="city">Faridabad</span><span class="view">View the listing</span></div></article>
      <article class="card"><div class="card-photo tone-c" role="img" aria-label="Glass retail complex"></div><h3>K7K Cosmopolitan</h3><div class="locality">Sector 66</div><div class="type">Shopping Complex</div><div class="card-foot"><span class="city">Gurgaon</span><span class="view">View the listing</span></div></article>
      <article class="card"><div class="card-photo tone-d" role="img" aria-label="Retail mall lit at dusk"></div><h3>Ovan 24K</h3><div class="locality">Sohna Road</div><div class="type">Retail Malls</div><div class="card-foot"><span class="city">Gurgaon</span><span class="view">View the listing</span></div></article>
      <article class="card"><div class="card-photo tone-a" role="img" aria-label="Residential retail tower"></div><h3>Magnora</h3><div class="locality">Adhan</div><div class="type">Shopping Complex</div><div class="card-foot"><span class="city">Surat</span><span class="view">View the listing</span></div></article>
      <article class="card"><div class="card-photo tone-b" role="img" aria-label="High street retail building"></div><h3>Veyra 81 High Street</h3><div class="locality">Sector 81</div><div class="type">Shopping Complex</div><div class="card-foot"><span class="city">Faridabad</span><span class="view">View the listing</span></div></article>
      <article class="card"><div class="card-photo tone-c" role="img" aria-label="Glass retail complex"></div><h3>K7K Cosmopolitan</h3><div class="locality">Sector 66</div><div class="type">Shopping Complex</div><div class="card-foot"><span class="city">Gurgaon</span><span class="view">View the listing</span></div></article>
      <article class="card"><div class="card-photo tone-d" role="img" aria-label="Retail mall lit at dusk"></div><h3>Ovan 24K</h3><div class="locality">Sohna Road</div><div class="type">Retail Malls</div><div class="card-foot"><span class="city">Gurgaon</span><span class="view">View the listing</span></div></article>
    </div>
  </div>
</section>

<section class="launches">
  <div class="wrap">
    <h2 class="section-title">Featured New Launches</h2>
    <div class="card-grid">
      <article class="card"><div class="card-photo tone-e" role="img" aria-label="Large shopping mall exterior"></div><h3>The Grand Indus Place</h3><div class="locality">Rahat Road</div><div class="type">Retail Malls</div><div class="card-foot"><span class="city">Bhopal</span><span class="view">View the listing</span></div></article>
      <article class="card"><div class="card-photo tone-c" role="img" aria-label="Modern retail tower"></div><h3>Crest One</h3><div class="locality">Sector 18</div><div class="type">Shopping Complex</div><div class="card-foot"><span class="city">Noida</span><span class="view">View the listing</span></div></article>
      <article class="card"><div class="card-photo tone-b" role="img" aria-label="City centre retail block"></div><h3>Core Heart - SCO In Sector</h3><div class="locality">Sahwa Wagre</div><div class="type">Retail Malls</div><div class="card-foot"><span class="city">Mohali</span><span class="view">View the listing</span></div></article>
      <article class="card"><div class="card-photo tone-d" role="img" aria-label="Retail mall lit at dusk"></div><h3>Ovan 24K</h3><div class="locality">Sohna Road</div><div class="type">Retail Malls</div><div class="card-foot"><span class="city">Gurgaon</span><span class="view">View the listing</span></div></article>
      <article class="card"><div class="card-photo tone-a" role="img" aria-label="Residential retail tower"></div><h3>Magnora</h3><div class="locality">Adhan</div><div class="type">Shopping Complex</div><div class="card-foot"><span class="city">Surat</span><span class="view">View the listing</span></div></article>
      <article class="card"><div class="card-photo tone-b" role="img" aria-label="High street retail building"></div><h3>Veyra 81 High Street</h3><div class="locality">Sector 81</div><div class="type">Shopping Complex</div><div class="card-foot"><span class="city">Faridabad</span><span class="view">View the listing</span></div></article>
      <article class="card"><div class="card-photo tone-c" role="img" aria-label="Glass retail complex"></div><h3>K7K Cosmopolitan</h3><div class="locality">Sector 66</div><div class="type">Shopping Complex</div><div class="card-foot"><span class="city">Gurgaon</span><span class="view">View the listing</span></div></article>
      <article class="card"><div class="card-photo tone-d" role="img" aria-label="Retail mall lit at dusk"></div><h3>Ovan 24K</h3><div class="locality">Sohna Road</div><div class="type">Retail Malls</div><div class="card-foot"><span class="city">Gurgaon</span><span class="view">View the listing</span></div></article>
    </div>
  </div>
</section>

<section class="widgets">
  <div class="wrap widget-row">
    <div class="mavens">
      <div class="widget-title">Lot Mavens</div>
      <p>Post your retail space requirement with us and our experts shall get back with suitable options and assist you through the deal. This is a free service.</p>
      <div class="input">Enter Your Email Address</div>
      <div class="input">Mobile</div>
      <div class="input textarea">Add Description Of Requirement</div>
      <span class="send">SEND</span>
    </div>
    <div class="plain-col">
      <div class="widget-title">Editor's Choice</div>
      <p>A "Select" Listing of Retail Properties Handpicked by our Editorial board of experts on their own positive parameters &amp; attributes such as Design Concept, Location, Developer Success Potential. So Read On to Check Out for yourself ........</p>
      <span class="send">SEND</span>
    </div>
    <div class="plain-col">
      <div class="widget-title">Listing Alert</div>
      <p>Subscribe for Fortnightly Email update on New Listings at Lotvantage</p>
      <div class="input">Enter Your Email Address</div>
      <div class="input">Select Area of Interest <svg width="8" height="6"><path d="M0 0h8L4 6z" fill="#ccc"/></svg></div>
      <div class="input">Select City of Interest <svg width="8" height="6"><path d="M0 0h8L4 6z" fill="#ccc"/></svg></div>
      <span class="send">SEND</span>
    </div>
  </div>
</section>

<footer>
  <section class="about-footer">
    <div class="wrap about-cols">
      <div>
        <h4>About Shopfront Hub</h4>
        <ul><li>Retail Malls</li><li>Shopping Complex</li><li>High Street Shops</li><li>Retail Warehouses</li></ul>
      </div>
      <div>
        <h4>www.lotvantage.com</h4>
        <p>Lotvantage.com, about us. Lotvantage.com is a specialised web based platform for retail space, featuring properties across India under various formats such as Retail Malls, Shopping Complexes, High-street Shops. Also featured are retail warehouses which provide the logistic back-end for the retail business. Lotvantage.com is useful to various category of users as follows.</p>
      </div>
      <div>
        <h4>Contact</h4>
        <p>Shopfront Hub<br>Unit 412, 4th Floor,<br>Lorem Ipsum Tower,<br>Sector 9, Gurgaon - 122000<br>Phone : 0000-000-0000<br>Fax : 0000 - 000 - 0000</p>
      </div>
    </div>
  </section>
  <section class="bottom-footer">
    <div class="footer-brand"><span class="brand-dot"></span><span class="brand-name">lotvantage</span></div>
    <div class="footer-links">Home | About Us | Privacy Policy | Site-map | Contact Us | Terms of Use</div>
    <div class="copyright">Copyright © 2013 Shopfront Hub.com. All rights reserved.</div>
    <div class="social"><span></span><span></span><span></span><span></span><span></span><span></span></div>
  </section>
</footer>

</body>
</html>
```